US Based Startup requires Website Design for Velmora Cell

We are launching a battery technology called "Velmora Cell" for which we need an elegant website design. We use red and black to represent positive and negative node color used in battery. The background is white. The font must provide more wide space and easy to read.
Velmora CellTM is a technology that uses fast switches, such as transistor switches, to make batteries more efficient. The novel technology can be implemented in all types of batteries – including non-rechargeable batteries, rechargeable batteries, wet-cell batteries and all metal oxide batteries.
Normal batteries are “non-switching”, that is, these batteries can only be connected to one another in parallel or series connections. Parallel connections enable batteries to charge faster whilst series connections enable the battery to discharge more efficiently to the load.
Velmora CellTM technology enables batteries to be connected in a third connection method called “duo-braidTM” that combines the benefit of faster charging of the batteries with renewable energy source, such as solar, in parallel connection, and then quickly re-configures the same batteries using the fast transistor switches, to be connected in series with the load, to discharge efficiently.

Target Market(s)

Renewable energy

Industry/Entity Type

Renewable

Coding

Coded - Design and coding required

Number of Pages Required

5+ page

Requirements
Must have
• The primary colors are red and black for logo and fonts. The background is white.
The font must be easy to read type of fonts with more white space. Only pictures will be in full color.
Nice to have
• Elegant and simple design bringing out a new battery concept to the energy industry.

```html
<!DOCTYPE html>
<html lang="en">
<head>
<meta charset="utf-8">
<title>Velmora Cell Inc</title>
<link rel="stylesheet" href="https://fonts.googleapis.com/css2?family=Montserrat:wght@300;400;500;600;700;800;900&display=swap">
<style>
:root{
  --red:#d1161c;
  --red-dark:#a30f14;
  --black:#111111;
  --ink:#1d1d1d;
  --grey-text:#777777;
  --grey-bg:#f3f3f3;
  --white:#ffffff;
}
*{margin:0;padding:0;box-sizing:border-box}
html,body{width:1200px;height:3884px;overflow:hidden}
body{font-family:"Montserrat",sans-serif;color:var(--ink);background:var(--white);position:relative}
.abs{position:absolute}
.btn{position:absolute;display:flex;align-items:center;justify-content:center;background:var(--red);color:var(--white);border-radius:30px;font-weight:700;text-transform:uppercase;letter-spacing:.3px}
.brand{display:flex;align-items:center;gap:10px;font-weight:800;color:var(--black);text-transform:uppercase;line-height:1}
.brand .dot{width:22px;height:22px;border-radius:50%;background:var(--red);flex:none}

/* header */
.site-header{position:absolute;top:0;left:0;width:1200px;height:88px;background:var(--white);border-top:4px solid var(--red);z-index:5}
.site-header .brand{position:absolute;left:144px;top:24px;font-size:22px}
.main-nav{position:absolute;left:472px;top:34px;display:flex;gap:30px;font-size:14px;font-weight:500}
.main-nav .active{color:var(--red)}
.login{left:956px;top:22px;width:100px;height:42px;font-size:15px}

/* hero */
.hero{position:absolute;top:88px;left:0;width:1200px;height:656px}
.hero-photo{position:absolute;inset:0;background:linear-gradient(180deg,#5c7fa6 0%,#9fb4c8 35%,#d9dde2 52%,#c9cfd6 62%,#23427f 78%,#1a2d5c 100%)}
.hero h1{position:absolute;left:144px;top:118px;color:var(--white);font-size:76px;line-height:84px;font-weight:900;letter-spacing:1px}
.hero h1 span{display:block;font-weight:400}
.hero .tagline{position:absolute;left:144px;top:300px;color:var(--white);font-size:27px;font-weight:600}
.hero-btn{left:144px;top:376px;width:176px;height:58px;font-size:18px}
.slider-dots{position:absolute;left:1128px;top:244px;display:flex;flex-direction:column;gap:9px}
.slider-dots i{width:9px;height:9px;border-radius:50%;background:var(--white)}
.slider-dots i.on{background:var(--red)}
.hero-cut{position:absolute;left:0;bottom:0}

/* about */
.about-mark{position:absolute;left:144px;top:780px;width:400px;height:410px;display:flex;align-items:center;justify-content:center;gap:16px}
.about-mark .dot{width:50px;height:50px;border-radius:50%;background:var(--red)}
.about-mark strong{font-size:44px;font-weight:800;color:var(--black);text-transform:uppercase;line-height:1.05}
.about-title{position:absolute;left:600px;top:770px;text-transform:uppercase}
.about-title h2{font-size:52px;font-weight:900;line-height:56px}
.about-title p{font-size:40px;font-weight:500;line-height:50px}
.red{color:var(--red)}
.about-copy{position:absolute;left:600px;top:896px;width:460px;font-size:13.5px;line-height:24px;color:var(--grey-text);font-weight:400}
.about-btn{left:600px;top:1143px;width:154px;height:51px;font-size:15px}

/* services */
.services{position:absolute;left:0;top:1205px;width:1200px;height:823px;background:var(--grey-bg)}
.services-scene{position:absolute;left:0;top:620px;width:1200px;height:200px;background:linear-gradient(180deg,rgba(243,243,243,1) 0%,#e3e6ea 60%,#dfe8da 100%)}
.section-title{position:absolute;left:0;width:1200px;text-align:center;font-size:50px;font-weight:900;text-transform:uppercase}
.section-title span{color:var(--red);font-weight:600}
.card{position:absolute;top:307px;width:216px;height:312px;background:var(--white);box-shadow:0 6px 18px rgba(0,0,0,.08);text-align:center}
.card svg{margin-top:40px}
.card h3{font-size:15px;font-weight:600;margin-top:18px;text-transform:uppercase}
.card p{font-size:12px;line-height:20px;color:var(--grey-text);margin:14px 18px 0}
.card .btn{left:50px;top:275px;width:116px;height:38px;font-size:11px}
.arrow{position:absolute;top:441px;width:44px;height:44px;border:1.5px solid #8a8a8a;border-radius:50%;background:var(--white);display:flex;align-items:center;justify-content:center}

/* projects */
.tile{position:absolute}
.view-btn{left:523px;top:2832px;width:154px;height:52px;font-size:15px}

/* contact */
.contact{position:absolute;left:0;top:2891px;width:1200px;height:800px}
.contact-bg{position:absolute;inset:0;background:linear-gradient(180deg,#b9161b 0%,#c81a20 45%,#a81217 100%)}
.contact .section-title{color:var(--white);top:200px}
.contact .section-title span{color:var(--white);font-weight:500}
.field{position:absolute;background:var(--white);border:none;font-family:inherit;font-size:15px;color:#333;padding:0 22px;display:flex;align-items:center}
.submit{left:523px;top:3463px;width:154px;height:50px;font-size:15px;background:var(--black)}

/* footer */
.site-footer{position:absolute;left:0;top:3640px;width:1200px;height:244px}
.site-footer .brand{position:absolute;left:162px;top:132px;font-size:30px;color:var(--white)}
.social{position:absolute;left:516px;top:70px;display:flex;gap:18px}
.social i{width:22px;height:22px;border-radius:50%;background:var(--white)}
.foot-nav{position:absolute;left:516px;top:120px;display:flex;gap:38px;font-size:17px;font-weight:600;color:var(--white)}
.copyright{position:absolute;left:516px;top:165px;font-size:12px;color:var(--white)}
</style>
</head>
<body>

<header class="site-header">
  <div class="brand"><span class="dot"></span>Velmora Cell Inc.</div>
  <nav class="main-nav">
    <span class="active">HOME</span><span>ABOUT</span><span>PRODUCTS</span><span>NEWS</span><span>CONTACT US</span>
  </nav>
  <span class="btn login">LOGIN</span>
</header>

<section class="hero">
  <div class="hero-photo" role="img" aria-label="Battery storage containers with solar panels and wind turbines under a cloudy sky"></div>
  <h1>VELMORA<span>CELL INC</span></h1>
  <p class="tagline">Lorem ipsum nsectetur adipiscing elit</p>
  <span class="btn hero-btn">GET STARTED</span>
  <div class="slider-dots"><i></i><i></i><i class="on"></i><i></i><i></i></div>
  <svg class="hero-cut" width="1200" height="130" viewBox="0 0 1200 130">
    <polygon points="0,130 0,124 305,40 1200,122 1200,130" fill="#ffffff"/>
    <polyline points="0,124 305,40 1200,122" fill="none" stroke="#d1161c" stroke-width="4"/>
  </svg>
</section>

<div class="about-mark"><span class="dot"></span><strong>Velmora<br>Cell</strong></div>
<div class="about-title"><h2>ABOUT</h2><p><span class="red">VELMORA</span> CELL</p></div>
<p class="about-copy">Lorem ipsum dolor sit amet, consectetur adipiscing ed do eiusmod tempor incididunt ut labore et dolore magna aliquuis ipsuspendisse ultricommodo viverra maecenas accumsan lacus vel facilisis.orem ipsum dolor sit amet, consectetur adipiscing ed do eiusmod tempor incididunt ut labore et dolore magna aliquuis ipsuspultricommodo viverra maecenas accumsan lacus vel facilisis. Lorem ipsum dolor sit amet, consectetur adipiscing ed do eiusmod tempor incididunt ut labore et dolore magna aliquuis ipsuspendisse ultricommodo viverra maecenas accumsan lacus vel facilisis.</p>
<span class="btn about-btn">READ MORE</span>

<section class="services">
  <svg class="abs" style="left:0;top:0" width="1200" height="120" viewBox="0 0 1200 120">
    <polygon points="0,0 1200,0 1200,0 895,115 0,45" fill="#ffffff"/>
    <polyline points="0,45 895,115 1200,0" fill="none" stroke="#d9d9d9" stroke-width="4"/>
  </svg>
  <div class="services-scene" role="img" aria-label="Faded landscape of solar panels, storage containers and power pylons"></div>
  <svg class="abs" style="left:0;top:700px" width="1200" height="123" viewBox="0 0 1200 123">
    <polygon points="0,123 0,115 305,28 1200,115 1200,123" fill="#ffffff"/>
  </svg>
  <h2 class="section-title" style="top:188px">OUR <span>SERVICES</span></h2>

  <div class="arrow" style="left:76px"><svg width="14" height="20" viewBox="0 0 14 20"><polyline points="11,2 3,10 11,18" fill="none" stroke="#333" stroke-width="2.5"/></svg></div>
  <div class="arrow" style="left:1079px"><svg width="14" height="20" viewBox="0 0 14 20"><polyline points="3,2 11,10 3,18" fill="none" stroke="#333" stroke-width="2.5"/></svg></div>

  <div class="card" style="left:143px">
    <svg width="80" height="80" viewBox="0 0 80 80" fill="none" stroke="#111" stroke-width="2.5"><path d="M20 55a25 25 0 0 1 18-40" stroke="#d1161c"/><path d="M60 25a25 25 0 0 1-18 40"/><rect x="32" y="26" width="16" height="28" rx="2"/><line x1="37" y1="34" x2="43" y2="34" stroke="#d1161c"/><line x1="37" y1="40" x2="43" y2="40" stroke="#d1161c"/><line x1="37" y1="46" x2="43" y2="46" stroke="#d1161c"/></svg>
    <h3>Excepteur Sint</h3>
    <p>Lorem ipsum dolor sit amet, consectetur adipiscing elit, sed do eiusmod ncididunt ut labore et dolore magna</p>
    <span class="btn">READ MORE</span>
  </div>
  <div class="card" style="left:375px">
    <svg width="80" height="80" viewBox="0 0 80 80" fill="none" stroke="#111" stroke-width="2.5"><rect x="22" y="6" width="36" height="68" rx="4"/><line x1="22" y1="16" x2="58" y2="16"/><path d="M34 32v8h12v-8M40 40v14" stroke="#d1161c"/><rect x="32" y="40" width="16" height="10" stroke="#d1161c"/></svg>
    <h3>Duis Aute</h3>
    <p>Lorem ipsum dolor sit amet, consectetur adipiscing elit, sed do eiusmod ncididunt ut labore et dolore magna</p>
    <span class="btn">READ MORE</span>
  </div>
  <div class="card" style="left:607px">
    <svg width="80" height="80" viewBox="0 0 80 80" fill="none" stroke="#111" stroke-width="2.5"><rect x="6" y="20" width="68" height="50" rx="3"/><rect x="14" y="12" width="10" height="8"/><rect x="56" y="12" width="10" height="8"/><path d="M18 45h8M22 41v8M54 45h8M42 32l-6 13h8l-6 13" stroke="#d1161c"/></svg>
    <h3>Magna Aliqu</h3>
    <p>Lorem ipsum dolor sit amet, consectetur adipiscing elit, sed do eiusmod ncididunt ut labore et dolore magna</p>
    <span class="btn">READ MORE</span>
  </div>
  <div class="card" style="left:840px">
    <svg width="80" height="80" viewBox="0 0 80 80" fill="none" stroke="#111" stroke-width="2.5"><rect x="8" y="16" width="30" height="58" rx="4"/><rect x="16" y="10" width="14" height="6"/><path d="M26 30l-8 14h10l-8 14" stroke="#d1161c"/><path d="M50 14v10M64 14v10M46 24h22v12a11 11 0 0 1-22 0zM57 47v14a10 10 0 0 1-19 3"/></svg>
    <h3>Commodo</h3>
    <p>Lorem ipsum dolor sit amet, consectetur adipiscing elit, sed do eiusmod ncididunt ut labore et dolore magna</p>
    <span class="btn">READ MORE</span>
  </div>
</section>

<h2 class="section-title" style="top:2075px">LATEST <span>PROJECTS</span></h2>
<div class="tile" style="left:143px;top:2190px;width:296px;height:293px;background:linear-gradient(180deg,#7f95ad 0%,#b8c3cf 50%,#d6d8da 100%)" role="img" aria-label="Solar canopy beside battery storage units"></div>
<div class="tile" style="left:452px;top:2190px;width:296px;height:293px;background:linear-gradient(160deg,#0d2c8a 0%,#2d66d6 45%,#9cc3f0 100%)" role="img" aria-label="Battery illustration with solar panels and wind turbines"></div>
<div class="tile" style="left:760px;top:2190px;width:296px;height:599px;background:linear-gradient(180deg,#7d8a8f 0%,#c9cfcf 40%,#e7e8e6 60%,#8e8f8c 100%)" role="img" aria-label="Battery storage cabinet on gravel"></div>
<div class="tile" style="left:143px;top:2496px;width:605px;height:293px;background:linear-gradient(180deg,#2d5675 0%,#b7b7b8 45%,#e5dfd6 60%,#3f6a2a 100%)" role="img" aria-label="Storage container with solar panels and wind turbines on grass"></div>
<span class="btn view-btn">VIEW MORE</span>

<section class="contact">
  <div class="contact-bg" role="img" aria-label="Red tinted storage containers in a landscape"></div>
  <svg class="abs" style="left:0;top:0" width="1200" height="120" viewBox="0 0 1200 120">
    <polygon points="0,0 1200,0 1200,0 305,115 0,18" fill="#ffffff"/>
    <polyline points="0,18 305,115 1200,0" fill="none" stroke="#111" stroke-width="3"/>
  </svg>
  <h2 class="section-title">CONTACT <span>FORM</span></h2>
</section>
<div class="field" style="left:234px;top:3190px;width:358px;height:52px">First Name</div>
<div class="field" style="left:605px;top:3190px;width:360px;height:52px">Last Name</div>
<div class="field" style="left:234px;top:3255px;width:358px;height:52px">Email address</div>
<div class="field" style="left:605px;top:3255px;width:360px;height:52px">Phone Number</div>
<div class="field" style="left:234px;top:3320px;width:731px;height:114px;align-items:flex-start;padding-top:18px">Message</div>
<span class="btn submit">SUBMIT</span>

<footer class="site-footer">
  <svg class="abs" style="left:0;top:0" width="1200" height="244" viewBox="0 0 1200 244">
    <polygon points="0,50 305,8 895,8 1200,50 1200,244 0,244" fill="#111111"/>
  </svg>
  <div class="brand"><span class="dot"></span>Velmora Cell Inc.</div>
  <div class="social" aria-label="Social links"><i></i><i></i><i></i></div>
  <nav class="foot-nav"><span>HOME</span><span>ABOUT</span><span>PRODUCTS</span><span>NEWS</span><span>CONTACT US</span></nav>
  <p class="copyright">© 2021 Velmora Cell All Rights Reserved &nbsp;|&nbsp; Privacy Policy &nbsp;|&nbsp; Terms and use</p>
</footer>

</body>
</html>
```